B2B Website for manufacturer of aerospace coatings

B2B Website for manufacturer of aerospace optical coatings and screens used in flight simulators and air-traffic controller centers. We sell to both the military as well as commercial airlines.

Colors: primary colors should be white and blue (same blue as in the logo), but you can accent with red, orange, or any other colors.

Main menu: Products, Services, About Us, Contact Us

Logo = See "Hollin SkyPrism" JPEG attached.

We'd like a professional website that appeals to engineers at companies like Varnell, OKTU, the military, etc.

We intend to build this website on WordPress.

Websites we like in our industry:
https://www.plaxomodel.example/
https://www.dorvik.example/civil-aviation/aviation-simulation-equipment/training-equipment/full-flight-simulators/
https://z7works.example/
https://www.lumbrent.example/
https://quellorn.example/
https://hangarpathworks.example/

3 Pages: Homepage, Product page, Contact Us page

Target Market(s)

Varnell, Pembry Falcrest, Zelvane

Industry/Entity Type

Aerospace

Number of Pages Required

3 page

Colors
0054AA
0677BA
7BADD7
CADEEF
E8F1F8
F0912C
F2A743
F7CA91
FBE8D2
FDF5EE
EB3D1F
EC4F4E
F09395
F8D3D4
FCEDEE

Requirements
Should not have
• Black background

```html
<!DOCTYPE html>
<html lang="en">
<head>
<meta charset="utf-8">
<title>Hollin SkyPrism</title>
<link rel="stylesheet" href="https://fonts.googleapis.com/css2?family=Exo+2:wght@400;500;600;700;800&display=swap">
<style>
:root{
  --blue:#0054AA;
  --blue-mid:#0677BA;
  --blue-soft:#7BADD7;
  --blue-pale:#E8F1F8;
  --ink:#14203a;
  --text:#4a5263;
  --navy:#0c1a33;
  --navy-line:#22335a;
  --white:#ffffff;
  --star:#F2A743;
}
*{margin:0;padding:0;box-sizing:border-box}
html,body{width:1200px;height:3976px;overflow:hidden}
body{font-family:"Exo 2",sans-serif;color:var(--ink);background:var(--white);position:relative}
.abs{position:absolute}
a{color:inherit;text-decoration:none}

/* top bar & header */
.topbar{top:0;right:0;height:34px;display:flex;gap:10px;padding-right:60px}
.pill{background:var(--blue);color:#fff;font-size:13px;display:flex;align-items:center;gap:6px;padding:0 14px;height:28px;border-radius:0 0 6px 6px}
.brand{top:30px;left:100px;color:var(--blue);font-weight:700;font-size:28px;line-height:1;white-space:nowrap}
.nav{top:52px;right:100px;display:flex;gap:34px;font-size:16px;font-weight:600}

/* hero */
.hero{top:92px;left:0;width:1200px;height:530px;background:linear-gradient(180deg,#5f6a72 0%,#2e3740 45%,#151b22 100%)}
.hero-shade{inset:0;background:linear-gradient(90deg,rgba(10,16,26,.75) 0%,rgba(10,16,26,.2) 60%,rgba(10,16,26,0) 100%)}
.hero-kicker{top:148px;left:100px;color:#fff;font-size:17px;font-weight:700;letter-spacing:.5px}
.hero-title{top:172px;left:100px;color:#fff;font-size:48px;font-weight:800;line-height:1.05}
.hero-sub{top:286px;left:100px;color:#fff;font-size:22px}
.btn{display:inline-flex;align-items:center;gap:8px;background:var(--blue);color:#fff;font-size:15px;font-weight:600;padding:0 20px;height:44px;border-radius:3px}
.hero .btn{position:absolute;top:326px;left:100px}
.dots{bottom:38px;left:562px;display:flex;gap:10px}
.dots span{width:9px;height:9px;border-radius:50%;background:rgba(255,255,255,.5)}
.dots span:first-child{background:#fff}
.scroll{top:210px;right:58px;writing-mode:vertical-rl;color:#fff;font-size:12px;letter-spacing:4px;font-weight:600}

/* about */
.about-kicker{top:772px;left:100px;font-size:17px;font-weight:700}
.about-title{top:790px;left:100px;font-size:52px;font-weight:800;color:var(--blue)}
.about-text{top:862px;left:100px;width:540px;font-size:15px;line-height:1.55;color:var(--text)}
.about .btn{position:absolute;top:1030px;left:100px}
.about-img{top:716px;left:700px;width:410px;height:420px;background:linear-gradient(135deg,#e9ecef,#9aa3ab 60%,#5a636b)}
.about-arc{top:690px;left:672px}

/* section headings */
.h2{font-size:58px;font-weight:800;text-align:center;left:0;width:1200px}
.h2 b{color:var(--ink);font-weight:800}
.h2 em{color:var(--blue);font-style:normal}

/* services */
.svc{top:1338px;width:325px;height:330px;border-radius:4px;overflow:hidden;background:linear-gradient(160deg,#c9cfd4,#6d7780 55%,#2a3038)}
.svc::after{content:"";position:absolute;inset:0;background:linear-gradient(180deg,rgba(0,0,0,0) 45%,rgba(0,0,0,.7))}
.svc h3{position:absolute;left:20px;bottom:58px;color:#fff;font-size:20px;font-weight:700;z-index:1}
.svc .more{position:absolute;left:20px;bottom:22px;color:#fff;font-size:15px;font-weight:600;display:flex;align-items:center;gap:8px;z-index:1}
.circle-arrow{width:24px;height:24px;border:1.5px solid #fff;border-radius:50%;display:inline-flex;align-items:center;justify-content:center}

/* testimonials */
.t-kicker{top:1782px;left:0;width:1200px;text-align:center;font-size:17px;font-weight:700;letter-spacing:1px}
.t-title{top:1810px;line-height:1.1;color:var(--blue)}
.tcard{background:#fff;box-shadow:0 6px 22px rgba(20,32,58,.15);padding:16px 20px;font-size:14px;line-height:1.5;color:var(--text)}
.who{display:flex;align-items:center;gap:10px;margin-bottom:8px}
.avatar{width:38px;height:38px;border-radius:50%;background:linear-gradient(135deg,#c8d3df,#7b8aa0)}
.who strong{display:block;color:var(--ink);font-size:16px}
.stars{color:var(--star);font-size:13px;letter-spacing:1px}

/* products */
.prod{top:2580px;width:302px}
.prod-img{height:228px;border-radius:24px 0 0 0;background:linear-gradient(150deg,#dfe3e7,#98a1a9 60%,#4b545c)}
.prod h3{margin-top:30px;font-size:20px;font-weight:800}
.prod p{margin-top:8px;font-size:15px;line-height:1.45;color:var(--text)}
.prod a{display:block;margin-top:18px;color:var(--blue);font-weight:700;font-size:15px}

/* contact */
.touch{top:3190px;left:100px;font-size:58px;font-weight:800;color:var(--ink)}
.touch span{color:var(--blue)}
.form{top:3272px;left:100px;width:570px;display:grid;grid-template-columns:1fr 1fr;gap:6px 6px}
.field{height:42px;border:1px solid #b8c2cf;font-size:14px;padding:10px 12px;color:var(--ink)}
.field.msg{grid-column:1/3;height:150px}
.form-btn{top:3528px;left:100px}
.touch-img{top:3200px;left:710px;width:490px;height:350px;border-radius:190px 0 0 190px;background:linear-gradient(180deg,#b8d2ec,#7aa3c9 55%,#4f6f8e)}

/* footer */
.footer{top:3600px;left:0;width:1200px;height:376px;background:var(--navy);color:#c9d2e2}
.f-brand{top:70px;left:100px;color:#fff;font-weight:700;font-size:24px;line-height:1;white-space:nowrap}
.social{top:150px;left:100px;display:flex;gap:10px}
.social span{width:34px;height:34px;border:1.5px solid #fff;border-radius:50%}
.fcol h4{color:#fff;font-size:18px;font-weight:700;margin-bottom:18px}
.fcol li{list-style:none;font-size:14px;margin-bottom:14px;display:flex;gap:8px;align-items:flex-start}
.news-input{width:270px;height:42px;border:1px solid var(--navy-line);background:#13244a;color:#8d9ab3;font-size:14px;padding:12px}
.news .btn{margin-top:8px;width:270px;justify-content:center}
.f-bottom{top:318px;left:100px;width:1000px;border-top:1px solid var(--navy-line);padding-top:20px;display:flex;justify-content:space-between;font-size:13px}
.f-bottom b{color:var(--blue-soft);font-weight:600}
</style>
</head>
<body>

<header>
  <div class="abs topbar">
    <span class="pill"><svg width="13" height="13" viewBox="0 0 24 24" fill="#fff"><path d="M6.6 10.8a15 15 0 0 0 6.6 6.6l2.2-2.2c.3-.3.7-.4 1-.2 1.1.4 2.3.6 3.6.6.6 0 1 .4 1 1V20c0 .6-.4 1-1 1A17 17 0 0 1 3 4c0-.6.4-1 1-1h3.5c.6 0 1 .4 1 1 0 1.3.2 2.5.6 3.6.1.3 0 .7-.2 1z"/></svg>555-014-2270</span>
    <span class="pill"><svg width="13" height="13" viewBox="0 0 24 24" fill="#fff"><path d="M2 5h20v14H2zm2 2v.5l8 5 8-5V7z"/></svg>info@hollinskyprism.example</span>
  </div>
  <a class="abs brand">Hollin SkyPrism</a>
  <nav class="abs nav"><a>About Us</a><a>Products</a><a>Services</a><a>Contact Us</a></nav>
</header>

<section class="abs hero" role="img" aria-label="Flight simulator cockpit with wraparound projection screen">
  <div class="abs hero-shade"></div>
  <p class="abs hero-kicker">OUR MISSION HAS ALWAYS BEEN TO</p>
  <h1 class="abs hero-title">PROVIDE THE HIGHEST<br>IMAGE FIDELITY</h1>
  <p class="abs hero-sub">to every project we undertake</p>
  <a class="btn">Explore More →</a>
  <div class="abs dots"><span></span><span></span><span></span></div>
  <div class="abs scroll">SCROLL DOWN</div>
</section>

<section class="about">
  <p class="abs about-kicker">ABOUT</p>
  <h2 class="abs about-title">HOLLIN LUMASCREEN</h2>
  <p class="abs about-text">Since Hollin Lumascreen's founding in 1947, Hollin has always been considered an optical house first that also happens to manufacture the world's largest "Seamless" front and back projection screens. Our mission has always been to provide the highest image fidelity to every project we undertake. In fact, the Academy of Screen Arts Guild.</p>
  <a class="btn">Read More →</a>
  <svg class="abs about-arc" width="120" height="120" viewBox="0 0 120 120"><path d="M14 120V70A56 56 0 0 1 70 14h50" fill="none" stroke="var(--blue)" stroke-width="14"/></svg>
  <div class="abs about-img" role="img" aria-label="Large seamless projection screen panel in the workshop"></div>
</section>

<section class="services">
  <h2 class="abs h2" style="top:1240px"><em>OUR</em> <b>SERVICES</b></h2>
  <div class="abs svc" style="left:100px" role="img" aria-label="Coated simulator dome interior"><h3>COATINGS AND SCREENS</h3><span class="more">Explore More <span class="circle-arrow">→</span></span></div>
  <div class="abs svc" style="left:438px" role="img" aria-label="Technician standing inside a projection dome"><h3>COATINGS AND SCREENS</h3><span class="more">Explore More <span class="circle-arrow">→</span></span></div>
  <div class="abs svc" style="left:776px" role="img" aria-label="Screen installation in a round simulator hall"><h3>COATINGS AND SCREENS</h3><span class="more">Explore More <span class="circle-arrow">→</span></span></div>
</section>

<section class="testimonials">
  <p class="abs t-kicker">TESTIMONIALS</p>
  <h2 class="abs h2 t-title">OVER 1,000 SATISFIED<br>CUTOMERS</h2>
  <svg class="abs" style="top:1982px;left:784px" width="90" height="70"><path d="M0 70V24A24 24 0 0 1 24 0h66v70z" fill="var(--blue)"/></svg>
  <svg class="abs" style="top:2160px;left:92px" width="70" height="90"><path d="M70 0A45 45 0 0 0 70 90z" fill="var(--blue)" transform="translate(-25 0)"/></svg>
  <svg class="abs" style="top:2295px;left:128px" width="30" height="30"><circle cx="15" cy="15" r="12" fill="none" stroke="var(--blue)" stroke-width="2"/></svg>
  <svg class="abs" style="top:2292px;left:890px" width="24" height="24"><path d="M12 3v18M3 12h18" stroke="var(--blue)" stroke-width="2"/></svg>

  <div class="abs tcard" style="top:2052px;left:112px;width:222px">
    <div class="who"><span class="avatar"></span><div><strong>Jon Dale</strong><span class="stars">★★★★★</span></div></div>
    Ultricies at vulputate lacinia, blandit porta odio. Morbi cursus cursus arcu, eu lobortis magna mollis at. Etiam tincidunt vulputate leo at ornare.
  </div>
  <div class="abs tcard" style="top:1996px;left:448px;width:220px">
    <div class="who"><span class="avatar"></span><div><strong>Alicia Marlow</strong><span class="stars">★★★★★</span></div></div>
    Morbi cursus cursus arcu, eu lobortis magna mollis at. Etiam tincidunt vulputate leo at ornare. Sed vel arcu.
  </div>
  <div class="abs tcard" style="top:2176px;left:448px;width:220px">
    <div class="who"><span class="avatar"></span><div><strong>Henry Jessop</strong><span class="stars">★★★★★</span></div></div>
    Ultricies at vulputate lacinia, blandit porta odio. Morbi cursus cursus arcu, eu lobortis magna mollis at. Etiam tincidunt vulputate leo at ornare.
  </div>
  <div class="abs tcard" style="top:2052px;left:792px;width:316px">
    <div class="who"><span class="avatar"></span><div><strong>Henry Jessop</strong><span class="stars">★★★★★</span></div></div>
    Ultricies at vulputate lacinia, blandit porta odio. Morbi cursus cursus arcu, eu lobortis magna mollis at. Etiam tincidunt vulputate leo at ornare.
  </div>
</section>

<section class="products">
  <h2 class="abs h2" style="top:2470px"><em>OUR</em> <b>PRODUCTS</b></h2>
  <article class="abs prod" style="left:100px">
    <div class="prod-img" role="img" aria-label="Compact projector module"></div>
    <h3>PRODUCT 01</h3>
    <p>Vestibulum pulvinar felis luctus posuere. Orci varius natoque penatibus et magnis dis parturient montes, nascetur ridiculus mus.</p>
    <a>Read More →</a>
  </article>
  <article class="abs prod" style="left:449px">
    <div class="prod-img" role="img" aria-label="Simulator cabin interior with screen"></div>
    <h3>PRODUCT 02</h3>
    <p>Vestibulum pulvinar felis luctus posuere. Orci varius natoque penatibus et magnis dis parturient montes, nascetur ridiculus mus.</p>
    <a>Read More →</a>
  </article>
  <article class="abs prod" style="left:798px">
    <div class="prod-img" role="img" aria-label="Dome simulator exterior in a hall"></div>
    <h3>PRODUCT 03</h3>
    <p>Vestibulum pulvinar felis luctus posuere. Orci varius natoque penatibus et magnis dis parturient montes, nascetur ridiculus mus.</p>
    <a>Read More →</a>
  </article>
</section>

<section class="contact">
  <h2 class="abs touch"><span>GET IN</span> TOUCH</h2>
  <form class="abs form">
    <div class="field">Name</div><div class="field">Email</div>
    <div class="field">Phone</div><div class="field">Location</div>
    <div class="field msg">Message</div>
  </form>
  <a class="abs btn form-btn">Submit Now →</a>
  <div class="abs touch-img" role="img" aria-label="Military helicopters in flight against the sky"></div>
</section>

<footer class="abs footer">
  <a class="abs f-brand">Hollin SkyPrism</a>
  <div class="abs social" aria-label="Social links"><span></span><span></span><span></span></div>
  <div class="abs fcol" style="top:60px;left:344px">
    <h4>CONTACT INFO</h4>
    <ul>
      <li><svg width="14" height="14" viewBox="0 0 24 24" fill="var(--blue-soft)"><path d="M12 2a7 7 0 0 0-7 7c0 5 7 13 7 13s7-8 7-13a7 7 0 0 0-7-7zm0 9.5A2.5 2.5 0 1 1 12 6.5a2.5 2.5 0 0 1 0 5z"/></svg><span>4791 Corbel Avenue<br>Dunmore, OH 43000</span></li>
      <li><svg width="14" height="14" viewBox="0 0 24 24" fill="var(--blue-soft)"><path d="M2 5h20v14H2zm2 2v.5l8 5 8-5V7z"/></svg>info@hollinskyprism.example</li>
      <li><svg width="14" height="14" viewBox="0 0 24 24" fill="var(--blue-soft)"><path d="M6.6 10.8a15 15 0 0 0 6.6 6.6l2.2-2.2c.3-.3.7-.4 1-.2 1.1.4 2.3.6 3.6.6.6 0 1 .4 1 1V20c0 .6-.4 1-1 1A17 17 0 0 1 3 4c0-.6.4-1 1-1h3.5c.6 0 1 .4 1 1 0 1.3.2 2.5.6 3.6.1.3 0 .7-.2 1z"/></svg>555-014-2270</li>
    </ul>
  </div>
  <div class="abs fcol" style="top:60px;left:632px">
    <h4>QUICK LINKS</h4>
    <ul><li>› About Us</li><li>› Products</li><li>› Services</li><li>› Contact Us</li></ul>
  </div>
  <div class="abs fcol news" style="top:60px;left:826px">
    <h4>NEWSLETTER</h4>
    <p style="font-size:14px;line-height:1.5;margin-bottom:14px">Nulla sed velit eros. Maecenas dui libero, convallis.</p>
    <div class="news-input">Enter email address</div>
    <a class="btn">Subscribe →</a>
  </div>
  <div class="abs f-bottom"><span>© 2022 <b>Hollin SkyPrism</b>. All right reserved</span><span>Dec 15, 2022 &nbsp; | &nbsp; Layout_4</span></div>
</footer>

</body>
</html>
```